Business card design - landscaping industry

Hello! We are very creative when it comes to landscape design but when it comes to designing business cards - not so much. We could use some help to come up with a design which is professional but fun. We are based in Grand Rapids, MI and work with high end properties for new landscape design and install. We are looking to have a template made for business card for a couple of us on staff.

You can get the flavor of our color scheme from our attached logo. We probably would want to highlight the green but also include some of the blue maybe.

Target Market(s)

We work with residential homeowners here in West Michigan. Very nice people by and large.

Industry/Entity Type

Landscaping

Contact Information for Business Card

The card should be standard size with round edges maybe?

Font styles to use
Serif
Sans Serif
Decorative

Requirements
Must have
• Must haves:
• 1. Address: 4817 Birchwell Meadow Lane SE, Grand Rapids, Michigan 49582
• 2. Phone: 616.555.0187
• 3. Email: company@larkhollowyard.com
• 4. URL: www.larkhollowyard.com
• 5. Names/Titles: (1) Dennis Harlow, President (2) Tomas Belvin, Director of Field Services
Nice to have
• On the back side of the card, we are thinking it would make sense to have a short listing of services offered...
• Landscape design & installation, Professional lawn maintenance, Spring & fall leaf cleanup, Irrigation system installation & maintenance, Snowplowing, Fertilizer & weed control, Tree maintenance and removal, Landscape bed maintenance
Should not have
• Our hope is that the design won't be too ostentatious. We are looking for professional and attractive.

```html
<!DOCTYPE html>
<html lang="en">
<head>
<meta charset="utf-8">
<title>Lark Hollow Landscaping – Business Card</title>
<link href="https://fonts.googleapis.com/css2?family=Cinzel:wght@600&family=Roboto+Condensed:wght@400;700&family=Work+Sans:wght@400;500&display=swap" rel="stylesheet">
<style>
  :root {
    --backdrop: #6e5842;
    --card-white: #ffffff;
    --brand-blue: #2a7fcb;
    --brand-navy: #1f5f9e;
    --brand-green: #4cb964;
    --text-dark: #3a3a3a;
    --blue-edge: #6cb7dc;
    --blue-core: #2a82c8;
  }
  * { margin: 0; padding: 0; box-sizing: border-box; }
  html, body { width: 1200px; height: 930px; overflow: hidden; }
  body { background: var(--backdrop); position: relative; font-family: "Work Sans", sans-serif; }

  .card {
    position: absolute;
    left: 278px;
    width: 645px;
    height: 368px;
    border-radius: 24px;
    overflow: hidden;
    box-shadow: 0 6px 18px rgba(0,0,0,0.35);
  }

  /* Front */
  .card-front { top: 76px; background: var(--card-white); }
  .front-brand {
    position: absolute; left: 36px; top: 72px;
    font-family: "Work Sans", sans-serif; font-weight: 500;
    font-size: 21px; letter-spacing: 3px; text-transform: uppercase;
    color: var(--brand-navy);
  }
  .holder-name {
    position: absolute; right: 37px; top: 144px;
    font-family: "Cinzel", serif; font-weight: 600;
    font-size: 30px; color: var(--brand-blue); line-height: 1;
  }
  .holder-rule {
    position: absolute; left: 36px; top: 188px;
    width: 486px; height: 2px; background: var(--brand-blue);
  }
  .holder-title {
    position: absolute; right: 37px; top: 178px;
    font-size: 16px; color: var(--text-dark); letter-spacing: 0.5px;
  }
  .accent-tab {
    position: absolute; right: 0; top: 150px;
    width: 16px; height: 45px;
    background: var(--brand-green);
    border-radius: 10px 0 0 10px;
  }
  .address {
    position: absolute; left: 36px; top: 230px;
    font-size: 16px; line-height: 20px; color: var(--text-dark);
  }
  .contacts {
    position: absolute; left: 36px; top: 280px;
    list-style: none; font-size: 16px; line-height: 20.5px; color: var(--text-dark);
  }
  .contacts li { display: flex; align-items: center; }
  .contacts svg { width: 10px; height: 10px; margin-right: 11px; flex: none; }
  .contacts .domain { color: var(--brand-blue); }

  /* Back */
  .card-back {
    top: 486px;
    background: linear-gradient(90deg, var(--blue-edge) 0%, var(--blue-core) 45%, var(--blue-core) 55%, var(--blue-edge) 100%);
    color: #fff; text-align: center;
  }
  .back-brand {
    position: absolute; left: 0; right: 0; top: 84px;
    font-family: "Work Sans", sans-serif; font-weight: 500;
    font-size: 34px; letter-spacing: 6px; text-transform: uppercase;
  }
  .services-heading {
    position: absolute; left: 0; right: 0; top: 186px;
    font-family: "Roboto Condensed", sans-serif; font-weight: 700;
    font-size: 22px;
  }
  .services-list {
    position: absolute; left: 0; right: 0; top: 240px;
    font-family: "Roboto Condensed", sans-serif; font-weight: 400;
    font-size: 17.5px; line-height: 21.5px;
  }
</style>
</head>
<body>

<section class="card card-front">
  <div class="front-brand">Lark Hollow Landscaping</div>
  <div class="holder-name">Dennis Harlow</div>
  <div class="holder-rule"></div>
  <div class="holder-title">President</div>
  <div class="accent-tab"></div>

  <address class="address" style="font-style:normal">
    4817 Birchwell Meadow Lane SE,<br>
    Grand Rapids, Michigan 49582
  </address>

  <ul class="contacts">
    <li>
      <svg viewBox="0 0 10 10"><path d="M2 1 L4 1 L4.5 3 L3.3 4 Q4.5 6 6 6.8 L7 5.6 L9 6.2 L9 8.2 Q5 9 2.2 5.5 Q1 3.5 2 1Z" fill="#2a7fcb"/></svg>
      616.555.0187
    </li>
    <li>
      <svg viewBox="0 0 10 10"><rect x="0.8" y="2" width="8.4" height="6" fill="none" stroke="#2a7fcb" stroke-width="1.2"/><path d="M1 2.4 L5 5.4 L9 2.4" fill="none" stroke="#2a7fcb" stroke-width="1.1"/></svg>
      company@larkhollowyard.com
    </li>
    <li>
      <svg viewBox="0 0 10 10"><circle cx="5" cy="5" r="4.2" fill="none" stroke="#2a7fcb" stroke-width="1"/><ellipse cx="5" cy="5" rx="1.8" ry="4.2" fill="none" stroke="#2a7fcb" stroke-width="0.9"/><path d="M1 5 H9" stroke="#2a7fcb" stroke-width="0.9"/></svg>
      <span>www.<span class="domain">larkhollowyard</span>.com</span>
    </li>
  </ul>
</section>

<section class="card card-back">
  <div class="back-brand">Lark Hollow Landscaping</div>
  <h2 class="services-heading">SERVICES OFFERED...</h2>
  <p class="services-list">
    Landscape design &amp; installation | Professional lawn maintenance<br>
    Spring &amp; fall leaf cleanup | Irrigation system installation &amp; maintenance<br>
    Snowplowing, Fertilizer &amp; weed control | Tree maintenance and removal<br>
    Landscape bed maintenance
  </p>
</section>

</body>
</html>
```